Gum Creek Critters business card and social media card

I would like 2 designs,

one with my logo that I have (attached file) for the front and then the chatterbook, Snapgallery and wanderguide icons on the back.I would like it to be eye catching.

The second design i would like the designers to come up with.I am looking for a colorful and eye catching but easy to read business card. I am in the center of Australia and would like earthy colors like orange/red, yellow, charcoal, brown, green etc. I would like a blue tongue lizard and a king brown snake in the design for the front. For the back I would like the Chatterbook, Snapgallery and wander guide logos.

Industry/Entity Type

Business

Contact Information for Business Card

Marcus Toller
CEO
GUM CREEK CRITTERS pty ltd
W: 041 907 2286
M: 048 216 0947
E: marcus@gumcreekcritters-example.com.au

Font styles to use
Other font styles liked:
• chiller

Colors
f37122
fbed22
ec1f27
474747
0492cd
acd036

Requirements
Must have
• Business name or my logo (attached file)
• Gum Creek Critters (in a cool font, like "chiller")
• Chatterbook icon
• Snapgallery icon
• Wanderguide icon
Nice to have
• Snake and a blue tongue lizard (either the full animals or just the heads)

```html
<!DOCTYPE html>
<html lang="en">
<head>
<meta charset="utf-8">
<title>Gum Creek Critters – Business Card</title>
<link rel="stylesheet" href="https://fonts.googleapis.com/css2?family=Patrick+Hand&display=swap">
<style>
  :root {
    --canvas-bg: #f6f6f6;
    --card-orange: #f37122;
    --panel-pink: #e8175d;
    --ink: #2b2b2b;
    --ink-blue: #2d3a55;
    --brand-brown: #5a1f1a;
    --title-red: #d0282a;
    --icon-green: #acd036;
    --social-blue: #0492cd;
    --white: #ffffff;
    --photo-light: #f1d6a4;
    --photo-mid: #d9a25e;
    --photo-dark: #8a5a2e;
  }
  * { box-sizing: border-box; margin: 0; padding: 0; }
  html, body {
    width: 1080px; height: 1200px; overflow: hidden;
    background: var(--canvas-bg);
    font-family: "Patrick Hand", cursive;
  }
  .canvas { position: relative; width: 1080px; height: 1200px; }

  /* Front card */
  .card-front {
    position: absolute; left: 72px; top: 41px; width: 934px; height: 549px;
    background: var(--card-orange); overflow: hidden;
  }
  .brand-panel {
    position: absolute; left: 0; top: 0; width: 372px; height: 100%;
    background: var(--panel-pink);
  }
  .brand-mark {
    position: absolute; left: 60px; top: 200px; width: 280px;
    display: flex; align-items: center; gap: 14px;
  }
  .brand-dot {
    flex: none; width: 46px; height: 46px; border-radius: 50%;
    background: var(--card-orange);
  }
  .brand-name {
    color: var(--brand-brown); font-size: 44px; line-height: 0.95;
    text-transform: uppercase; letter-spacing: 1px;
  }
  .person-name {
    position: absolute; left: 372px; width: 562px; top: 50px;
    text-align: center; font-size: 66px; color: var(--ink);
    letter-spacing: 1px; line-height: 1;
  }
  .person-role {
    position: absolute; left: 372px; width: 562px; top: 146px;
    text-align: center; font-size: 54px; color: var(--ink); line-height: 1;
  }
  .company {
    position: absolute; left: 418px; top: 276px;
    font-size: 29px; color: var(--ink-blue); letter-spacing: 0.5px;
  }
  .contact-icon {
    position: absolute; left: 351px; width: 42px; height: 42px;
  }
  .contact-icon.phone { top: 351px; }
  .contact-icon.mail  { top: 414px; }
  .phones {
    position: absolute; left: 414px; top: 334px;
    font-size: 29px; line-height: 30px; color: var(--ink-blue); letter-spacing: 2px;
  }
  .email {
    position: absolute; left: 418px; top: 414px;
    font-size: 27px; color: var(--ink-blue); letter-spacing: 0.5px;
  }

  /* Back card */
  .card-back {
    position: absolute; left: 68px; top: 646px; width: 939px; height: 500px;
    background: var(--card-orange); border: 1.5px solid var(--panel-pink);
  }
  .animal-artwork {
    position: absolute; left: 124px; top: 62px; width: 600px; height: 198px;
    border-radius: 90px;
    background: radial-gradient(ellipse at 40% 50%, var(--photo-light), var(--photo-mid) 60%, var(--photo-dark));
    opacity: 0.9;
  }
  .back-title {
    position: absolute; left: 0; width: 100%; top: 278px; padding-right: 24px;
    text-align: center; font-size: 46px; color: var(--title-red); letter-spacing: 2px;
  }
  .socials {
    position: absolute; top: 346px; left: 0; width: 100%;
  }
  .social {
    position: absolute; width: 160px; margin-left: -80px;
    display: flex; flex-direction: column; align-items: center; gap: 6px;
  }
  .social-dot {
    width: 88px; height: 80px; border-radius: 50%; background: var(--social-blue);
  }
  .social-name { font-size: 22px; color: var(--white); }
</style>
</head>
<body>
<div class="canvas">

  <section class="card-front">
    <div class="brand-panel">
      <div class="brand-mark">
        <span class="brand-dot"></span>
        <span class="brand-name">Gum Creek<br>Critters</span>
      </div>
    </div>

    <h1 class="person-name">MARCUS TOLLER</h1>
    <p class="person-role">CEO</p>
    <p class="company">GUM CREEK CRITTERS pty ltd</p>

    <svg class="contact-icon phone" viewBox="0 0 42 42" aria-hidden="true">
      <circle cx="21" cy="21" r="21" fill="var(--icon-green)"/>
      <path d="M14 12c1.5-1 3 0 4 2l1 2c.5 1-.2 2-1 2.6-.6.4-.6 1.2 0 2.2 1 1.6 2.2 2.8 3.6 3.6 1 .6 1.8.6 2.2 0 .6-.8 1.6-1.5 2.6-1l2 1c2 1 3 2.5 2 4-1.5 2.5-4 3-7 1.5-4-2-7.5-5.5-9.5-9.5-1.5-3-1-5.5 1.1-7.4z" fill="var(--white)"/>
      <path d="M24 13a6 6 0 0 1 5 5M24 9a10 10 0 0 1 9 9" stroke="var(--white)" stroke-width="1.8" fill="none" stroke-linecap="round"/>
    </svg>
    <div class="phones">
      <div>W: 041 907 2286</div>
      <div>M: 048 216 0947</div>
    </div>

    <svg class="contact-icon mail" viewBox="0 0 42 42" aria-hidden="true">
      <circle cx="21" cy="21" r="21" fill="var(--icon-green)"/>
      <rect x="11" y="14" width="20" height="14" rx="1.5" fill="var(--white)"/>
      <path d="M11.5 14.5 21 22l9.5-7.5" stroke="var(--icon-green)" stroke-width="1.6" fill="none"/>
    </svg>
    <p class="email">marcus@gumcreekcritters-example.com.au</p>
  </section>

  <section class="card-back">
    <div class="animal-artwork" role="img" aria-label="Photograph of a coiled pale yellow python beside a blue tongue lizard"></div>
    <h2 class="back-title">GUM CREEK CRITTERS</h2>
    <div class="socials">
      <div class="social" style="left:216px">
        <span class="social-dot"></span>
        <span class="social-name">Chatterbook</span>
      </div>
      <div class="social" style="left:464px">
        <span class="social-dot"></span>
        <span class="social-name">Snapgallery</span>
      </div>
      <div class="social" style="left:712px">
        <span class="social-dot"></span>
        <span class="social-name">Wanderguide</span>
      </div>
    </div>
  </section>

</div>
</body>
</html>
```